Nutritional neuroscience book cover design*

We need a book cover design for a new book on nutritional neuroscience and aging. The book is written for the general public and answers questions such as, "We are living longer than ever. The problem is, will our brain stay healthy as we age? We certainly do not want to live longer with various diseases, in particular brain diseases. How does the brain change during aging? And what can we do to promote the health of our brain and prevent and treat neurological diseases that typically occur during the aging process?" Based on recent discoveries in the field of nutritional neuroscience, this book presents how we can use nutrition to help our brain stay healthy longer. While our brain shrinks and becomes functionally weaker during the aging process, nutrition is able to slow this process down. This book illustrates this point through chapters on stroke, Parkinson’s disease, Multiple Sclerosis, dementia, depression, anxiety, and schizophrenia. The book will appeal to anyone looking to optimize their brain’s health and performance today and decades into the future.

Target Market(s)

General audience

Colors

Designer to choose colors to be used in the design.

Requirements
Must have
• Title: Meals Across the Decades: A Field Guide to Diet and the Mind
• Edited by Corinne T. Halvorsen, Ph.D.
• Book size: 7*10 inches
• Backcover text:
• Humans are living longer than ever. How does the brain change during aging? Will our brain stay healthy as we age? We certainly do not want to live longer with neurological diseases. What can we do to promote the health of our brain?
• Based on recent discoveries in the field of nutritional neuroscience, this book presents how nutrition affects our brain health. While we age, our brain shrinks and there are changes in how it functions, nutrition is an important component that can help maintain optimal brain health.
• Using scientific evidence, this book illustrates the importance of nutrition for neurological diseases including Alzheimer’s disease, stroke, Parkinson’s disease, Multiple Sclerosis, vascular dementia, depression, anxiety, and schizophrenia. This book will appeal to anyone looking to learn more about how nutrition affects brain health.

```html
<!DOCTYPE html>
<html lang="en">
<head>
<meta charset="utf-8">
<title>Meals Across the Decades — Book Cover</title>
<link href="https://fonts.googleapis.com/css2?family=Marcellus&family=Cormorant+Garamond:wght@500;600&family=Raleway:ital,wght@1,300&display=swap" rel="stylesheet">
<style>
  :root {
    --page-bg: #f4f4f2;
    --cover-bg: #f7f6f3;
    --forest: #3e5c38;
    --forest-dark: #34502f;
    --sage: #6f7f4a;
    --ink-soft: #4a5a44;
    --white: #ffffff;
    --tomato: #e0452e;
    --citrus: #f29a3a;
    --leaf: #6f9a3c;
    --plum: #8e4a9c;
  }
  * { margin: 0; padding: 0; box-sizing: border-box; }
  html, body {
    width: 1200px;
    height: 1106px;
    overflow: hidden;
    background: var(--page-bg);
  }
  .canvas {
    position: relative;
    width: 1200px;
    height: 1106px;
  }
  .cover {
    position: absolute;
    left: 245px;
    top: 38px;
    width: 710px;
    height: 1030px;
    background: var(--cover-bg);
    box-shadow: 0 10px 30px rgba(0,0,0,0.12);
    overflow: hidden;
  }
  .title-block {
    position: absolute;
    top: 52px;
    left: 0;
    right: 0;
    text-align: center;
    color: var(--forest);
  }
  .title-lead {
    font-family: "Cormorant Garamond", serif;
    font-weight: 600;
    font-size: 40px;
    line-height: 1;
  }
  .title-main {
    font-family: "Marcellus", serif;
    font-size: 112px;
    line-height: 1;
    margin-top: 8px;
    letter-spacing: 1px;
    text-transform: uppercase;
  }
  .subtitle {
    font-family: "Raleway", sans-serif;
    font-style: italic;
    font-weight: 300;
    font-size: 29px;
    color: var(--ink-soft);
    margin-top: 18px;
  }
  .artwork {
    position: absolute;
    left: 0;
    top: 350px;
    width: 710px;
    height: 600px;
  }
  .author-band {
    position: absolute;
    left: 0;
    right: 0;
    bottom: 0;
    height: 92px;
    background: var(--forest);
    display: flex;
    align-items: center;
    justify-content: center;
  }
  .author-name {
    font-family: "Cormorant Garamond", serif;
    font-weight: 600;
    font-size: 46px;
    color: var(--white);
    letter-spacing: 0.5px;
  }
</style>
</head>
<body>
<main class="canvas">
  <section class="cover">
    <header class="title-block">
      <p class="title-lead">Meals Across the</p>
      <h1 class="title-main">Decades</h1>
      <p class="subtitle">A Field Guide to Diet and the Mind</p>
    </header>

    <svg class="artwork" viewBox="0 0 710 600" role="img"
         aria-label="Photograph of a white plate printed with a tree shaped like a brain, ringed by fresh vegetables and fruit: tomatoes, green onions, banana, purple and orange cauliflower, grapefruit and orange halves">
      <defs>
        <radialGradient id="produce-ring" cx="50%" cy="50%" r="50%">
          <stop offset="0%" stop-color="#ffffff"/>
          <stop offset="52%" stop-color="#eeeeea"/>
          <stop offset="62%" stop-color="#d9a06a"/>
          <stop offset="78%" stop-color="#c9553f"/>
          <stop offset="92%" stop-color="#8f9a5a"/>
          <stop offset="100%" stop-color="#f7f6f3"/>
        </radialGradient>
      </defs>
      <ellipse cx="360" cy="300" rx="330" ry="300" fill="url(#produce-ring)"/>
    </svg>

    <footer class="author-band">
      <p class="author-name">Corinne T. Halvorsen</p>
    </footer>
  </section>
</main>
</body>
</html>
```